Innovative, creative, and beautiful simple book cover!

I’ve spend 5 years writing a book about executive consulting. Last task of the project is to find the best possible cover and I need help from you guys.

In the book, I take the liberty of creating a model which secures successful sales throughout the value chain, driven by the top management.

For you info, I used Pixel Harbor once before and of cause ended buying a logo. In short I’m here to buy the best book cover idea - and look forward to see what genius ideas you can bring to the table.

Thank you very much.
Torvald

P.S. Please see my brief in attach documents. .
Updates

Target Market(s)

Business people en general

Industry/Entity Type

Management Consulting

Font styles to use
Sans Serif

Requirements
Must have
• - My attach files about description for front page and back page have to be incorporated.
• - BOTH A FRONT, SPINE AND A BACK PAGE!
• - Please see all my attach files – the project is very well described and should be ready to work on.
• - The idea about the “building line” is an idea I love, but if you have something else you think I should see – try me.
Nice to have
• I love simple, minimalistic design
Should not have
• I don't like old fashion or over designed solutions. Sorry :-)

```html
<!DOCTYPE html>
<html lang="en">
<head>
<meta charset="UTF-8">
<title>Boardroom Sales Excellence — Book Cover</title>
<link rel="stylesheet" href="https://fonts.googleapis.com/css2?family=Bebas+Neue&family=Cinzel:wght@400&display=swap">
<style>
  :root {
    --page-bg: #ffffff;
    --cover-bg: #f4f4f4;
    --title-red: #e31b1b;
    --ink: #111111;
    --skyline-dark: #1a1a1a;
    --skyline-mid: #6b6b6b;
    --skyline-light: #c9c9c9;
  }
  * { margin: 0; padding: 0; box-sizing: border-box; }
  html, body {
    width: 1200px;
    height: 1200px;
    overflow: hidden;
    background: var(--page-bg);
  }
  .canvas {
    position: relative;
    width: 1200px;
    height: 1200px;
    background: var(--page-bg);
  }
  .cover {
    position: absolute;
    left: 219px;
    top: 27px;
    width: 762px;
    height: 1146px;
    background: var(--cover-bg);
    overflow: hidden;
  }
  .title {
    position: absolute;
    left: 0;
    width: 100%;
    text-align: center;
    font-family: "Bebas Neue", "Oswald", sans-serif;
    font-weight: 400;
    color: var(--title-red);
    line-height: 1;
    white-space: nowrap;
  }
  .title-line-1 {
    top: 99px;
    font-size: 116px;
    letter-spacing: 4px;
  }
  .title-line-2 {
    top: 193px;
    font-size: 177px;
    letter-spacing: 2px;
  }
  .subtitle {
    position: absolute;
    left: 0;
    top: 398px;
    width: 100%;
    text-align: center;
    font-family: "Bebas Neue", "Oswald", sans-serif;
    font-size: 37px;
    line-height: 54px;
    letter-spacing: 0.08em;
    color: var(--ink);
    white-space: nowrap;
  }
  .skyline {
    position: absolute;
    left: 0;
    top: 754px;
    width: 100%;
    height: 76px;
    background: linear-gradient(to bottom,
      rgba(201,201,201,0) 0%,
      var(--skyline-light) 35%,
      var(--skyline-mid) 70%,
      var(--skyline-dark) 100%);
  }
  .ground-line {
    position: absolute;
    left: 0;
    top: 830px;
    width: 100%;
    height: 14px;
    background: var(--skyline-dark);
  }
  .author {
    position: absolute;
    left: 0;
    top: 1042px;
    width: 100%;
    text-align: center;
    font-family: "Cinzel", "Times New Roman", serif;
    font-size: 46px;
    letter-spacing: 0.04em;
    color: var(--ink);
    white-space: nowrap;
  }
</style>
</head>
<body>
  <div class="canvas">
    <div class="cover">
      <h1>
        <span class="title title-line-1">BOARDROOM SALES</span>
        <span class="title title-line-2">EXCELLENCE</span>
      </h1>
      <p class="subtitle">DELIVER WINNING SALES ACROSS EVERY<br>STAGE OF THE BUSINESS, LED BY THE BOARDROOM</p>
      <div class="skyline" role="img" aria-label="Black and grey silhouette of a city skyline with a ferris wheel, bridge, domes and towers"></div>
      <div class="ground-line"></div>
      <p class="author">TORVALD BRANDT</p>
    </div>
  </div>
</body>
</html>
```